Storm Restoration Contractor needs a professional business card design

Looking for a professional business card design. Not looking for your cheapo MS Word standard ones that are readily available. Dont want it to be cookie cutter look like ones readily available online. We just recently changed our logo and want to freshen up all our documents. Our company handles restoring a property back to a pre-loss condition after a storm damages it. For example, wind, hail, flood, fire losses.

Target Market(s)

Property Owners, Homeowners, Property Owners, Commercial Property Owners, Property Management Companies, Hail and Wind Damaged Properties

Industry/Entity Type

Construction Company

Contact Information for Business Card

Brightline Facades
847-555-0193
847-555-0147 fax
www.brightlinefacades.example
info@brightlinefacades.example

Requirements
Must have
• Clean, Professional, fresh look
• Storm Restoration, Roofing, Siding, Windows
Nice to have
• If there is a way to incorporate storms that may be cool.

```html
<!DOCTYPE html>
<html lang="en">
<head>
<meta charset="utf-8">
<title>Brightline Facades – Business Card</title>
<link href="https://fonts.googleapis.com/css2?family=Montserrat:wght@300;400;600&display=swap" rel="stylesheet">
<style>
  :root {
    --backdrop: #8a7866;
    --card-dark: #212121;
    --card-band: #ededed;
    --card-white: #ffffff;
    --brand-blue: #1a7fc4;
    --ink: #2b2b2b;
    --map-grey: #ececec;
    --storm-deep: #1c2230;
    --storm-mid: #4d5a78;
    --storm-warm: #8a6a45;
  }
  * { margin: 0; padding: 0; box-sizing: border-box; }
  html, body { width: 1200px; height: 801px; overflow: hidden; }
  body {
    background: var(--backdrop);
    font-family: "Montserrat", sans-serif;
    position: relative;
  }
  .card {
    position: absolute;
    top: 273px;
    width: 480px;
    height: 267px;
    overflow: hidden;
    box-shadow: 0 3px 8px rgba(0,0,0,0.35);
  }
  /* Front */
  .card-front { left: 110px; background: var(--card-dark); }
  .card-front .band {
    position: absolute; left: 0; right: 0; bottom: 0; height: 52px;
    background: var(--card-band);
  }
  .brand {
    position: absolute; left: 46px; top: 60px;
    display: flex; align-items: center; gap: 16px;
  }
  .brand-dot {
    width: 78px; height: 78px; border-radius: 50%;
    border: 5px solid var(--brand-blue);
  }
  .brand-name {
    color: var(--brand-blue);
    font-weight: 600;
    font-size: 36px;
    line-height: 1.05;
    letter-spacing: 2px;
    text-transform: uppercase;
  }
  /* Back */
  .card-back { left: 635px; background: var(--card-white); }
  .map-area {
    position: absolute; left: 40px; top: 10px; width: 210px; height: 250px;
    background: radial-gradient(ellipse at center, var(--map-grey) 0%, rgba(236,236,236,0) 70%);
  }
  .contact {
    position: absolute; left: 26px; top: 106px;
    width: 226px;
    color: var(--ink); font-size: 10.5px; font-weight: 400;
    white-space: nowrap;
  }
  .contact-row { display: flex; align-items: center; gap: 9px; margin-bottom: 12px; }
  .contact-row p { line-height: 14px; }
  .icon {
    flex: 0 0 auto;
    width: 25px; height: 25px; border: 1.5px solid var(--brand-blue);
    border-radius: 50%; display: flex; align-items: center; justify-content: center;
  }
  .storm-photo {
    position: absolute; right: 0; top: 0; width: 222px; height: 267px;
    background:
      radial-gradient(ellipse at 75% 15%, var(--storm-warm) 0%, rgba(138,106,69,0) 45%),
      radial-gradient(ellipse at 35% 85%, #8ea6d8 0%, rgba(142,166,216,0) 45%),
      linear-gradient(170deg, var(--storm-deep) 0%, var(--storm-mid) 60%, #6f7fa3 100%);
  }
  .corner-flag {
    position: absolute; right: 0; top: 0; width: 0; height: 0;
    border-top: 50px solid var(--brand-blue);
    border-left: 50px solid transparent;
  }
</style>
</head>
<body>
  <section class="card card-front" aria-label="Card front">
    <div class="brand">
      <div class="brand-dot"></div>
      <div class="brand-name">Brightline<br>Facades</div>
    </div>
    <div class="band"></div>
  </section>

  <section class="card card-back" aria-label="Card back">
    <div class="map-area" role="img" aria-label="Faint world map background"></div>
    <div class="contact">
      <div class="contact-row">
        <span class="icon">
          <svg width="12" height="12" viewBox="0 0 24 24"><path fill="#2b2b2b" d="M6.6 10.8c1.4 2.8 3.8 5.1 6.6 6.6l2.2-2.2c.3-.3.7-.4 1-.2 1.1.4 2.3.6 3.6.6.6 0 1 .4 1 1V20c0 .6-.4 1-1 1C10.6 21 3 13.4 3 4c0-.6.4-1 1-1h3.5c.6 0 1 .4 1 1 0 1.3.2 2.5.6 3.6.1.3 0 .7-.2 1z"/></svg>
        </span>
        <p>847-555-0193<br>847-555-0147 FAX</p>
      </div>
      <div class="contact-row">
        <span class="icon">
          <svg width="13" height="13" viewBox="0 0 24 24"><circle cx="12" cy="12" r="9" fill="none" stroke="#2b2b2b" stroke-width="2"/><path d="M3 12h18M12 3c3 3 3 15 0 18M12 3c-3 3-3 15 0 18" fill="none" stroke="#2b2b2b" stroke-width="1.6"/></svg>
        </span>
        <p>www.brightlinefacades.example<br>info@brightlinefacades.example</p>
      </div>
    </div>
    <div class="storm-photo" role="img" aria-label="Photo of dark storm clouds with lightning"></div>
    <div class="corner-flag"></div>
  </section>
</body>
</html>
```